Powerpoint for Talveo

Check out the attached sample powerpoint, we would like our powerpoint to look similar to this. in the slides where you see monitor, we would like to put pics of different industries in each monitor. like images of hotels, hospitals, large business with multiple locations, small business, retail)

The Powerpoint will contain the below slides

About US
Our Guarantee – 100% satisfaction and 30% cost savings
Products & Services ( Hosted PBX phone system, SIP Trunking, Network security solutions, commercial grade band width and firewalls, IT Network design services)
Features ( One slide for this we will enter the content)
Industries ( Small business, hospitality, hospitals, Banks for secure voice, Large business with multiple locations, Retail)
Hosted PBX
Why Talveo
Channel partners
Our customers
Contact us
Updates

Target Market(s)

Small business, hospitality, hospitals, Banks for secure voice, Large business with multiple locations, Retail, law firms, insurance companies

Industry/Entity Type

Security

Requirements
Must have
• Please look at the attached powerpoint for color, style, font details

```html
<!DOCTYPE html>
<html lang="en">
<head>
<meta charset="utf-8">
<title>Talveo Presentation Template</title>
<link rel="stylesheet" href="https://fonts.googleapis.com/css2?family=Cinzel:wght@400;700&family=Graduate&display=swap">
<style>
  :root {
    --page: #ffffff;
    --frame: #3a3a3a;
    --sky-light: #7fd0f4;
    --sky: #3aaee6;
    --ocean: #1c7fcf;
    --deep: #0b4f8f;
    --teal-dark: #0a5878;
    --band-light: #8cc4ec;
    --accent: #1a86d0;
    --ink: #1a1a1a;
    --body-ink: #3a3a3a;
    --white: #ffffff;
  }
  * { box-sizing: border-box; margin: 0; padding: 0; }
  html, body { width: 1200px; height: 900px; overflow: hidden; background: var(--page); }
  body { position: relative; font-family: "Cinzel", serif; color: var(--ink); }

  .slide {
    position: absolute; left: 285px; width: 701px; height: 394px;
    border: 1px solid var(--frame); background: var(--page);
  }
  .slide--cover { top: 22px; }
  .slide--content { top: 435px; }

  .cover-banner {
    position: absolute; left: 19px; top: 11px; width: 658px; height: 162px;
    background:
      radial-gradient(ellipse 60% 40% at 45% 45%, rgba(255,255,255,.35), transparent 70%),
      linear-gradient(100deg, var(--sky-light) 0%, var(--sky) 45%, var(--ocean) 80%, #2364b4 100%);
  }
  .accent-band {
    position: absolute; left: 19px; width: 658px;
    background: linear-gradient(90deg, var(--band-light) 0%, #1a9ad6 45%, var(--teal-dark) 100%);
  }
  .slide--cover .accent-band { top: 175px; height: 16px; }

  .corner-mark { position: absolute; left: 19px; bottom: 14px; width: 50px; height: 50px; }
  .corner-mark svg { display: block; }
  .page-number {
    position: absolute; left: 9px; bottom: 4px; font-family: "Graduate", serif;
    font-size: 20px; color: var(--white); line-height: 1;
  }

  .brand {
    position: absolute; display: flex; align-items: center; gap: 5px;
    font-family: "Cinzel", serif; font-weight: 700; color: var(--ink); line-height: 1;
  }
  .brand__dot { border-radius: 50%; background: var(--accent); }
  .slide--cover .brand { right: 24px; bottom: 30px; font-size: 21px; }
  .slide--cover .brand__dot { width: 16px; height: 16px; }
  .slide--content .brand { right: 18px; bottom: 24px; font-size: 11px; gap: 3px; }
  .slide--content .brand__dot { width: 9px; height: 9px; }

  .title-band {
    position: absolute; left: 19px; top: 11px; width: 663px; height: 57px;
    display: flex; align-items: center; justify-content: center;
    background:
      radial-gradient(ellipse 50% 60% at 30% 80%, rgba(160,220,250,.35), transparent 70%),
      linear-gradient(90deg, #2f9fe0 0%, #1d78c4 40%, var(--deep) 100%);
  }
  .title-band__text {
    font-family: "Graduate", serif; font-size: 38px; color: var(--white);
    letter-spacing: 1px; padding-left: 26px;
  }
  .slide--content .accent-band { top: 72px; height: 6px; }

  .content {
    position: absolute; left: 41px; top: 104px; width: 420px;
  }
  .content__title {
    font-family: "Cinzel", serif; font-weight: 400; font-size: 17px; color: var(--ink);
    margin-bottom: 9px;
  }
  .content__lead { position: relative; padding-left: 31px; }
  .content__chevron { position: absolute; left: 0; top: 0; }
  .content__text {
    font-size: 5.6px; line-height: 7.6px; color: var(--body-ink);
    margin-bottom: 8px; width: 390px;
  }
  .content__lead .content__text { width: 388px; }
</style>
</head>
<body>

  <section class="slide slide--cover" aria-label="Cover slide">
    <div class="cover-banner" role="img" aria-label="Abstract light blue background with soft flowing light waves"></div>
    <div class="accent-band"></div>
    <div class="corner-mark">
      <svg width="50" height="50" viewBox="0 0 50 50"><polygon points="0,0 50,50 0,50" fill="var(--accent)"/></svg>
    </div>
    <div class="brand"><span class="brand__dot"></span>Talveo</div>
  </section>

  <section class="slide slide--content" aria-label="Content slide">
    <div class="title-band" role="img" aria-label="Blue header band with soft light waves">
      <h1 class="title-band__text">TITLE PAGE</h1>
    </div>
    <div class="accent-band"></div>

    <article class="content">
      <h2 class="content__title">Content Title</h2>
      <div class="content__lead">
        <svg class="content__chevron" width="23" height="22" viewBox="0 0 23 22">
          <polygon points="0,0 13,0 23,11 13,22 0,22 9,11" fill="var(--sky)"/>
        </svg>
        <p class="content__text">Our team designs secure voice and data networks for offices of every size. We plan each system with care, install it on schedule and support it every day of the year. Clients gain clear calls, steady bandwidth and strong firewalls, while monthly costs fall. Every project begins with a careful review of current lines, devices and contracts, so the new setup fits the way people already work.</p>
      </div>
      <p class="content__text">Our team designs secure voice and data networks for offices of every size. We plan each system with care, install it on schedule and support it every day of the year. Clients gain clear calls, steady bandwidth and strong firewalls, while monthly costs fall. Every project begins with a careful review of current lines, devices and contracts, so the new setup fits the way people already work.</p>
      <p class="content__text">Our team designs secure voice and data networks for offices of every size. We plan each system with care, install it on schedule and support it every day of the year. Clients gain clear calls, steady bandwidth and strong firewalls, while monthly costs fall. Every project begins with a careful review of current lines, devices and contracts, so the new setup fits the way people already work.</p>
      <p class="content__text">Our team designs secure voice and data networks for offices of every size. We plan each system with care, install it on schedule and support it every day of the year. Clients gain clear calls, steady bandwidth and strong firewalls, while monthly costs fall. Every project begins with a careful review of current lines, devices and contracts, so the new setup fits the way people already work.</p>
    </article>

    <div class="corner-mark">
      <svg width="50" height="50" viewBox="0 0 50 50"><polygon points="0,0 50,50 0,50" fill="var(--accent)"/></svg>
      <span class="page-number">1</span>
    </div>
    <div class="brand"><span class="brand__dot"></span>Talveo</div>
  </section>

</body>
</html>
```